Add words, element to an already make product design

Hi guys,
I m already have the design (attached) which is a wet tissue product. The front main side (about 14cm x 7 cm) is the waves and the brand name Vorra. However, in this main side, it should contain more words, which are "Khan uot" (mean wet wipe), and the words "Mat lanh" (mean cooling) and "Tinh khiet" (mean purity). "Khan uot" to indicate function of the product, while Mat lanh and Tinh khiet are just marketing term to add.
So yes, the task is quite simple, but I think the key is to choose an appropriate font, color and the location you decide where it should be. You can add any element you want, as long as it look good overall, and those words above, are required to have. More in the attached are few rival from our market, as some example.
Thank you, and wait your idea.

Hi guys, Just to tell you that the main front design will not change. So the waves and the brand name still keep the same. Just adding more words or elements to it. Thank you guys.

```html
<!DOCTYPE html>
<html lang="vi">
<head>
<meta charset="utf-8">
<title>Vorra – Khan uot front panel</title>
<link rel="stylesheet" href="https://fonts.googleapis.com/css2?family=Nunito:wght@800;900&display=swap">
<style>
  :root {
    --navy: #0f2a4d;
    --navy-deep: #0b1a30;
    --sky: #4fc3ec;
    --sky-light: #a9dcf4;
    --steel: #a9c3d8;
    --sea: #1f86c4;
    --paper: #ffffff;
    --mist: #eef2f6;
  }
  html, body {
    margin: 0;
    width: 881px;
    height: 1200px;
    overflow: hidden;
    background: var(--paper);
  }
  .canvas {
    position: relative;
    width: 881px;
    height: 1200px;
  }
  .front-panel {
    position: absolute;
    left: 93px;
    top: 426px;
    width: 695px;
    height: 347px;
    box-shadow: 0 2px 6px rgba(15, 42, 77, 0.18);
  }
  .front-panel svg { display: block; }
  .brand-name {
    font-family: "Nunito", sans-serif;
    font-weight: 900;
    font-size: 78px;
    fill: var(--navy);
  }
  .product-type {
    font-family: "Nunito", sans-serif;
    font-weight: 900;
    font-size: 27px;
    fill: var(--paper);
  }
  .benefit-label {
    font-family: "Nunito", sans-serif;
    font-weight: 900;
    font-size: 17px;
    fill: var(--navy);
  }
</style>
</head>
<body>
<main class="canvas">
  <section class="front-panel" aria-label="Vorra wet wipes front panel">
    <svg width="695" height="347" viewBox="0 0 695 347" xmlns="http://www.w3.org/2000/svg">
      <defs>
        <linearGradient id="paperTone" x1="0" y1="0" x2="1" y2="1">
          <stop offset="0" stop-color="#ffffff"/>
          <stop offset="0.5" stop-color="#f6f8fa"/>
          <stop offset="1" stop-color="#eceff2"/>
        </linearGradient>
        <linearGradient id="seaTone" x1="0" y1="0" x2="0" y2="1">
          <stop offset="0" stop-color="#8fd3f2"/>
          <stop offset="0.35" stop-color="#e6f5fc"/>
          <stop offset="0.6" stop-color="#7cc2e6"/>
          <stop offset="1" stop-color="#1a7fbf"/>
        </linearGradient>
        <linearGradient id="bannerTone" x1="0" y1="0" x2="1" y2="0">
          <stop offset="0" stop-color="#6fd0f2"/>
          <stop offset="1" stop-color="#3fbbe8"/>
        </linearGradient>
        <radialGradient id="badgeTone" cx="0.5" cy="0.5" r="0.5">
          <stop offset="0.6" stop-color="#ffffff"/>
          <stop offset="1" stop-color="#8fd6f5"/>
        </radialGradient>
      </defs>

      <rect class="panel-ground" width="695" height="347" fill="url(#paperTone)"/>

      <path class="sea-visual" role="img" aria-label="Watercolour sea waves with a white box of wet wipes"
            d="M400,0 C360,50 342,120 368,190 C388,250 362,310 350,347 L695,347 L695,0 Z"
            fill="url(#seaTone)"/>

      <path class="wave-band" d="M372,0 L402,0 C360,50 342,120 368,190 C388,250 362,310 350,347 L318,347 C342,300 352,250 338,200 C318,130 328,55 372,0 Z"
            fill="var(--navy-deep)"/>
      <path class="wave-line" d="M357,8 C318,60 300,120 325,195 C342,250 325,305 310,347"
            fill="none" stroke="var(--steel)" stroke-width="7"/>

      <text class="brand-name" x="155" y="138" text-anchor="middle">Vorra</text>

      <path class="type-banner" d="M36,192 C55,168 95,158 150,160 C205,162 245,160 268,148 C262,178 238,198 195,200 C140,202 85,188 36,192 Z"
            fill="url(#bannerTone)"/>
      <text class="product-type" x="155" y="190" text-anchor="middle">Khan uot</text>

      <g class="benefit benefit-cooling">
        <circle cx="86" cy="250" r="25" fill="url(#badgeTone)" stroke="var(--sky)" stroke-width="2"/>
        <path d="M86,236 C80,246 76,252 76,257 A10,10 0 0 0 96,257 C96,252 92,246 86,236 Z"
              fill="none" stroke="var(--sea)" stroke-width="1.6"/>
        <text class="benefit-label" x="86" y="299" text-anchor="middle">MAT LANH</text>
      </g>

      <g class="benefit benefit-purity">
        <circle cx="227" cy="250" r="25" fill="url(#badgeTone)" stroke="var(--sky)" stroke-width="2"/>
        <path d="M227,236 C221,246 217,252 217,257 A10,10 0 0 0 237,257 C237,252 233,246 227,236 Z"
              fill="none" stroke="var(--sea)" stroke-width="1.6"/>
        <text class="benefit-label" x="227" y="299" text-anchor="middle">TINH KHIET</text>
      </g>
    </svg>
  </section>
</main>
</body>
</html>
```